psd/html for a e Paylume website designed

hi
i am in need of a psd / html for a whole website designed
the site is a e wallet /payment system i can i will provide a link to what type of style i am looking for but i can not stress this enough i do not want anyone replicating the website i am just providing the links to show you what kind of function and the content that is involved also, i have a srs with detailed pages you can read and refer to if need be
thanks of viewing
Vantoleaf.com
Brisklune.com
marblequivercoin.com
Qrdelivane.com

```html
<!DOCTYPE html>
<html lang="en">
<head>
<meta charset="utf-8">
<title>Paylume</title>
<link rel="stylesheet" href="https://fonts.googleapis.com/css2?family=Bebas+Neue&family=Open+Sans:ital,wght@0,400;0,700;0,800;1,400&family=Comfortaa:wght@400&display=swap">
<style>
:root{
  --sky:#3db8dc;
  --sky-dark:#0b8db8;
  --footer:#0a98cb;
  --footer-bar:#0a79a6;
  --band:#e8e8e8;
  --ink:#3f3f3f;
  --body:#555;
  --white:#fff;
}
*{margin:0;padding:0;box-sizing:border-box}
html,body{width:823px;height:1200px;overflow:hidden;background:var(--white)}
body{position:relative;font-family:"Open Sans",Arial,sans-serif;color:var(--body)}
.abs{position:absolute}
.hero-bg{position:absolute;left:0;top:0;width:823px;height:560px}
.brand{left:103px;top:24px;color:var(--white);font-weight:700;font-size:26px;line-height:30px;letter-spacing:-.3px}
.btn{top:25px;height:27px;width:78px;border-radius:14px;background:linear-gradient(#f2f2f2,#c9c9c9);border:1px solid #e6e6e6;box-shadow:0 1px 2px rgba(0,0,0,.25);font-weight:700;font-size:11.5px;color:#4a4a4a;text-align:center;line-height:25px;letter-spacing:.3px}
.nav{top:78px;left:99px;height:25px;display:flex}
.nav a{color:var(--white);text-decoration:none;font-weight:700;font-size:9.5px;line-height:25px;letter-spacing:.1px;padding:0 14.5px;margin-right:-2px}
.nav a.active{background:var(--sky-dark)}
.slider{left:96px;top:108px;width:631px;height:270px;background:var(--white);border-radius:3px;box-shadow:0 2px 4px rgba(0,0,0,.2)}
.slider-shadow{left:130px;top:372px;width:563px;height:20px;border-radius:50%;background:radial-gradient(ellipse at center,rgba(0,0,0,.35),rgba(0,0,0,0) 70%)}
.slide-photo{left:7px;top:7px;width:617px;height:255px;background:linear-gradient(100deg,#e9ecec 0%,#d9dfdf 35%,#c4cfd0 60%,#e7eced 100%)}
.slide-title{left:24px;top:68px;font-family:"Comfortaa",sans-serif;font-size:47px;color:var(--sky);letter-spacing:-.5px}
.slide-text{left:29px;top:128px;width:275px;font-size:9.6px;line-height:15.5px;color:#222}
.dots{top:395px;left:401px;display:flex;gap:3px}
.dots i{width:4px;height:4px;border-radius:50%;background:#ccc;display:block}
.dots i.on{background:#888}
.welcome{top:414px;left:0;width:823px;text-align:center;font-family:"Bebas Neue",sans-serif;font-weight:400;font-size:32px;color:var(--ink)}
.welcome span{color:var(--sky)}
.welcome-text{top:458px;left:100px;width:624px;text-align:center;font-size:9.9px;letter-spacing:-.1px;line-height:15.5px;color:var(--body)}
.features{top:557px;left:0;width:823px;height:255px;background:var(--band)}
.features::before{content:"";position:absolute;left:120px;right:120px;top:-6px;height:10px;border-radius:50%;box-shadow:0 3px 5px rgba(0,0,0,.18)}
.feature{width:200px;height:90px}
.feature svg{position:absolute;left:0;top:0}
.feature h3{position:absolute;left:51px;top:1px;font-family:"Bebas Neue",sans-serif;font-weight:400;font-size:16.5px;line-height:14.5px;color:var(--ink)}
.feature p{position:absolute;left:51px;top:39px;width:150px;font-size:9px;line-height:11.8px;color:var(--body)}
.news-head{top:843px;left:343px;display:flex;align-items:center;gap:9px;font-family:"Bebas Neue",sans-serif;font-size:27px;color:var(--ink)}
.news{width:200px;height:60px}
.news .thumb{position:absolute;left:0;top:0;width:45px;height:45px;background:linear-gradient(135deg,#7c95b8,#c9d3de 55%,#9aa9c0);border:1px solid #ccc}
.news h4{position:absolute;left:55px;top:-3px;font-size:9px;font-weight:700;color:#222}
.news p{position:absolute;left:55px;top:11px;width:145px;font-size:9px;line-height:11.8px}
.news a{position:absolute;left:55px;top:47px;font-family:Georgia,serif;font-style:italic;font-size:8.5px;color:var(--sky);text-decoration:none}
.footer{top:1000px;left:0;width:823px;height:170px;background:var(--footer);color:var(--white)}
.footer h5{position:absolute;font-family:"Bebas Neue",sans-serif;font-weight:400;font-size:13.5px;letter-spacing:.3px}
.links{position:absolute;top:42px;font-size:8.6px;line-height:15px}
.social{position:absolute;top:45px;left:478px;display:flex;gap:4px}
.social i{display:block;width:23px;height:23px;border-radius:50%;background:var(--white)}
.contact{position:absolute;left:600px;font-size:9px}
.contact b{font-size:10.5px}
.badge{position:absolute;border-radius:3px}
.footer-bar{top:1170px;left:0;width:823px;height:30px;background:var(--footer-bar);color:var(--white);font-size:8.8px;line-height:28px}
.footer-bar .copy{position:absolute;left:100px}
.footer-bar nav{position:absolute;right:96px}
.footer-bar nav span{margin:0 7px;opacity:.8}
</style>
</head>
<body>

<svg class="hero-bg" viewBox="0 0 823 560" aria-hidden="true">
  <defs>
    <linearGradient id="creamFade" x1="0" y1="0" x2="0" y2="1">
      <stop offset="0" stop-color="#fffbe8"/>
      <stop offset="1" stop-color="#ffffff"/>
    </linearGradient>
  </defs>
  <rect width="823" height="560" fill="url(#creamFade)"/>
  <path d="M0 0H823V288C650 274 420 262 250 272C140 278 60 286 0 296Z" fill="#3db8dc"/>
</svg>

<div class="abs brand">Paylume</div>
<div class="abs btn" style="left:560px">SIGN UP</div>
<div class="abs btn" style="left:643px">LOG IN</div>

<nav class="abs nav">
  <a class="active" href="#">HOME</a>
  <a href="#">PERSONAL ACCOUNTS</a>
  <a href="#">BUSINESS ACCOUNTS</a>
  <a href="#">BEGINNER'S GUIDE</a>
  <a href="#">DEVELOPERS</a>
  <a href="#">HELP CENTRE</a>
</nav>

<div class="abs slider-shadow"></div>
<section class="abs slider">
  <div class="abs slide-photo" role="img" aria-label="Hands typing on a keyboard while holding a payment card"></div>
  <div class="abs slide-title">Buy Online</div>
  <p class="abs slide-text">Lorem ipsum dolor sit amet, consectetur adipisicing elit, sed do eiusmod tempor incididunt ut labore et dolore magna aliqua. Ut enim ad minim veniam, quis nostrud exercitation ullamco laboris nisi ut aliquip</p>
</section>
<div class="abs dots"><i></i><i class="on"></i><i></i></div>

<h1 class="abs welcome">WELCOME TO <span>PAYLUME</span></h1>
<p class="abs welcome-text">Lorem ipsum dolor sit amet, consectetur adipisicing elit, sed do eiusmod tempor incididunt ut labore et dolore magna aliqua. Ut enim ad minim veniam, quis nostrud exercitation ullamco laboris nisi ut aliquip ex ea commodo consequat. Duis aute irure dolor in reprehenderit in voluptate velit esse cillum dolore eu fugiat nulla pariatur. Excepteur sint occaecat cupidatat non proident, sunt in culpa qui officia deserunt mollit anim id est laborum.</p>

<section class="abs features">
  <div class="abs feature" style="left:97px;top:43px">
    <svg width="42" height="34" viewBox="0 0 42 34" fill="none" stroke="#3db8dc" stroke-width="4.5" stroke-linecap="round"><path d="M3 12Q21 -2 39 12"/><path d="M10 19Q21 10 32 19"/><circle cx="21" cy="28" r="3" fill="#3db8dc" stroke="none"/></svg>
    <h3>INSTANT<br>TRANSACTIONS</h3>
    <p>Lorem ipsum dolor sit amet, consectetur adipisicing elit, sed do eiusmod tempor.</p>
  </div>
  <div class="abs feature" style="left:315px;top:43px">
    <svg width="40" height="40" viewBox="0 0 40 40" fill="none" stroke="#3db8dc" stroke-width="3"><circle cx="19" cy="19" r="17" fill="#3db8dc"/><path d="M4 16Q12 12 16 18T12 30M22 4Q20 12 28 14T34 26" stroke="#fff" stroke-width="2.5"/></svg>
    <h3>SAFE<br>ONLINE ENVIRONMENT</h3>
    <p>Lorem ipsum dolor sit amet, consectetur adipisicing elit, sed do eiusmod tempor.</p>
  </div>
  <div class="abs feature" style="left:533px;top:43px">
    <svg width="40" height="34" viewBox="0 0 40 34"><rect x="2" y="2" width="35" height="30" rx="4" fill="#3db8dc"/><rect x="6" y="8" width="27" height="19" rx="2" fill="none" stroke="#fff" stroke-width="2"/><rect x="24" y="13" width="13" height="9" rx="3" fill="#fff"/><circle cx="29" cy="17.5" r="2" fill="#3db8dc"/></svg>
    <h3>MULTIPLE<br>WALLETS</h3>
    <p>Lorem ipsum dolor sit amet, consectetur adipisicing elit, sed do eiusmod tempor.</p>
  </div>
  <div class="abs feature" style="left:97px;top:148px">
    <svg width="40" height="40" viewBox="0 0 40 40"><path d="M6 3L13 2L17 12L12 16Q17 26 24 30L28 25L38 29L37 36Q34 39 28 38Q8 30 2 10Q2 5 6 3Z" fill="#3db8dc"/></svg>
    <h3>GREAT<br>CUSTOMER SUPPORT</h3>
    <p>Lorem ipsum dolor sit amet, consectetur adipisicing elit, sed do eiusmod tempor.</p>
  </div>
  <div class="abs feature" style="left:315px;top:148px">
    <svg width="40" height="40" viewBox="0 0 40 40"><path d="M32 20A13 13 0 1 1 24 8" fill="none" stroke="#3db8dc" stroke-width="7"/><path d="M20 1L34 8L22 17Z" fill="#3db8dc"/></svg>
    <h3>EASY<br>TO DEPOSIT AND WITHDRAW</h3>
    <p>Lorem ipsum dolor sit amet, consectetur adipisicing elit, sed do eiusmod tempor.</p>
  </div>
  <div class="abs feature" style="left:533px;top:148px">
    <svg width="40" height="42" viewBox="0 0 40 42"><path d="M13 2H27L24 9H16Z" fill="#3db8dc"/><path d="M16 11H24L30 34L20 41L10 34Z" fill="#3db8dc"/><path d="M14 18L26 14M13 25L28 20M12 32L29 27" stroke="#e8e8e8" stroke-width="2"/></svg>
    <h3>RESIDUAL<br>AFFILIATE INCOME</h3>
    <p>Lorem ipsum dolor sit amet, consectetur adipisicing elit, sed do eiusmod tempor.</p>
  </div>
</section>

<div class="abs news-head">
  <svg width="26" height="26" viewBox="0 0 26 26"><rect x="1" y="2" width="20" height="22" rx="2" fill="#3db8dc"/><rect x="18" y="8" width="7" height="16" rx="2" fill="#3db8dc"/><rect x="5" y="6" width="12" height="5" fill="#fff"/><path d="M5 14H17M5 17H17M5 20H13" stroke="#fff" stroke-width="1.6"/></svg>
  <span>LATEST NEWS</span>
</div>

<article class="abs news" style="left:97px;top:898px">
  <div class="thumb" role="img" aria-label="News thumbnail image"></div>
  <h4>Lorem ipsum dolor</h4>
  <p>Lorem ipsum dolor sit amet, consectetur adipisicing elit, sed do eiusmod tempor.</p>
  <a href="#">[Readmore...]</a>
</article>
<article class="abs news" style="left:314px;top:898px">
  <div class="thumb" role="img" aria-label="News thumbnail image"></div>
  <h4>Lorem ipsum dolor</h4>
  <p>Lorem ipsum dolor sit amet, consectetur adipisicing elit, sed do eiusmod tempor.</p>
  <a href="#">[Readmore...]</a>
</article>
<article class="abs news" style="left:531px;top:898px">
  <div class="thumb" role="img" aria-label="News thumbnail image"></div>
  <h4>Lorem ipsum dolor</h4>
  <p>Lorem ipsum dolor sit amet, consectetur adipisicing elit, sed do eiusmod tempor.</p>
  <a href="#">[Readmore...]</a>
</article>

<footer class="abs footer">
  <h5 style="left:96px;top:21px">QUICK LINKS</h5>
  <div class="links" style="left:96px">About Us<br>How it works<br>Blog</div>
  <div class="links" style="left:166px">Sell Online<br>Buy Online<br>Affiliate Program</div>
  <div class="links" style="left:249px">Support<br>F.A.Q.<br>Fees<br>Terms</div>
  <div class="links" style="left:299px">Developers<br>Application Programming Interface<br>Shopping Cart Interface</div>

  <h5 style="left:477px;top:21px">SOCIAL MEDIA</h5>
  <div class="social"><i></i><i></i><i></i></div>

  <h5 style="left:600px;top:21px">CONTACT INFO</h5>
  <div class="contact" style="top:45px">PHONE</div>
  <div class="contact" style="top:59px"><b>(555) 310 4477 182</b></div>
  <div class="contact" style="top:88px">EMAIL</div>
  <div class="contact" style="top:102px"><b>info@paylume.net</b></div>

  <div class="badge" style="left:97px;top:107px;width:76px;height:48px;background:#e8e8e8;border:2px solid #c33"></div>
  <div class="badge" style="left:187px;top:107px;width:74px;height:36px;background:#fff;border:2px solid #bbb"></div>
  <div class="badge" style="left:273px;top:107px;width:91px;height:43px;background:#f2f2f2;border:2px solid #ddd"></div>
</footer>

<div class="abs footer-bar">
  <span class="copy">© 2013 Paylume</span>
  <nav>Home<span>|</span>Merchants<span>|</span>Exchangers<span>|</span>Fees<span>|</span>Terms<span>|</span>F.A.Q.<span>|</span>Developers</nav>
</div>

</body>
</html>
```